'Tarvoon' a financial/crypto-currency exchange in the middle east

On the card we need 1) Name 2) title 3) email address 4) phone number using the same colors and theme as the logo. On one side we just want the logo and we want the whole card to be in blue (same blue as logo) with the logo in the back being white.
Industry/Entity Type
Financial

```html
<!DOCTYPE html>
<html lang="en">
<head>
<meta charset="utf-8">
<title>Tarvoon Business Card</title>
<link rel="stylesheet" href="https://fonts.googleapis.com/css2?family=Open+Sans:wght@400;600&display=swap">
<style>
  :root {
    --page-bg: #eceef1;
    --card-blue: #1a77c0;
    --card-blue-deep: #0f68ad;
    --brand-silver: #e4e7ea;
    --text-white: #ffffff;
    --text-soft: #e3eef8;
    --mark-white: rgba(255, 255, 255, 0.92);
  }
  html, body {
    margin: 0;
    padding: 0;
    width: 1200px;
    height: 970px;
    overflow: hidden;
    background: var(--page-bg);
    font-family: "Open Sans", sans-serif;
  }
  .canvas {
    position: relative;
    width: 1200px;
    height: 970px;
  }
  .card {
    position: absolute;
    left: 100px;
    top: 207px;
    width: 1000px;
    height: 556px;
    border-radius: 28px;
    background: linear-gradient(135deg, var(--card-blue) 0%, var(--card-blue-deep) 100%);
    overflow: hidden;
    box-shadow: 0 10px 30px rgba(20, 40, 70, 0.18);
  }
  .brand-name {
    position: absolute;
    left: 48px;
    top: 62px;
    margin: 0;
    font-size: 84px;
    font-weight: 600;
    line-height: 1;
    color: var(--brand-silver);
    letter-spacing: 1px;
  }
  .person {
    position: absolute;
    left: 50px;
    top: 208px;
  }
  .person-name {
    margin: 0;
    font-size: 27px;
    font-weight: 600;
    color: var(--text-white);
    letter-spacing: 0.5px;
    line-height: 1.2;
  }
  .person-title {
    margin: 2px 0 0;
    font-size: 23px;
    font-weight: 400;
    color: var(--text-soft);
    line-height: 1.2;
  }
  .contact-list {
    position: absolute;
    left: 50px;
    top: 300px;
    margin: 0;
    padding: 0;
    list-style: none;
  }
  .contact-item {
    display: flex;
    align-items: center;
    height: 31px;
    font-size: 22px;
    color: var(--text-white);
  }
  .contact-icon {
    width: 20px;
    height: 20px;
    margin-right: 10px;
    fill: var(--text-white);
  }
  .contact-address {
    margin-top: 6px;
  }
  .social {
    position: absolute;
    left: 50px;
    top: 470px;
    display: flex;
    align-items: center;
    font-size: 22px;
    font-weight: 600;
    color: var(--text-white);
  }
  .social-dot {
    width: 22px;
    height: 22px;
    border-radius: 50%;
    background: var(--text-white);
    margin-right: 10px;
  }
  .mark {
    position: absolute;
    left: 440px;
    top: 6px;
    width: 544px;
    height: 544px;
  }
</style>
</head>
<body>
<div class="canvas">
  <section class="card">
    <h1 class="brand-name">Tarvoon</h1>

    <div class="person">
      <p class="person-name">LENA MARSH</p>
      <p class="person-title">Managing Director</p>
    </div>

    <ul class="contact-list">
      <li class="contact-item">
        <svg class="contact-icon" viewBox="0 0 20 20"><path d="M3 7c0-2 3-4 7-4s7 2 7 4v2h-4V7.5c-1-.6-5-.6-6 0V9H3z"/><rect x="4" y="10" width="12" height="7" rx="1.5"/></svg>
        + 000 000 000
      </li>
      <li class="contact-item">
        <svg class="contact-icon" viewBox="0 0 20 20"><path d="M6 1h8a1.5 1.5 0 0 1 1.5 1.5v15A1.5 1.5 0 0 1 14 19H6a1.5 1.5 0 0 1-1.5-1.5v-15A1.5 1.5 0 0 1 6 1zm0.5 2v12h7V3z"/></svg>
        + 000 000 000
      </li>
      <li class="contact-item">
        <svg class="contact-icon" viewBox="0 0 20 20"><path d="M2 4h16v12H2z M3.5 5.5 10 10.5l6.5-5" fill="none" stroke="#fff" stroke-width="1.6"/></svg>
        Lena@tarvoon.com
      </li>
      <li class="contact-item">
        <svg class="contact-icon" viewBox="0 0 20 20"><circle cx="10" cy="10" r="7.5" fill="none" stroke="#fff" stroke-width="1.6"/><path d="M2.5 10h15M10 2.5c-3 3-3 12 0 15M10 2.5c3 3 3 12 0 15" fill="none" stroke="#fff" stroke-width="1.4"/></svg>
        www.tarvoon.com
      </li>
      <li class="contact-item contact-address">215 Harlow Ave, FL 33910</li>
    </ul>

    <div class="social">
      <span class="social-dot"></span>
      @Tarvoon
    </div>

    <svg class="mark" viewBox="0 0 544 544" role="img" aria-label="Tarvoon emblem">
      <circle cx="272" cy="272" r="258" fill="var(--mark-white)"/>
      <text x="272" y="300" text-anchor="middle" font-family="'Open Sans', sans-serif" font-size="84" font-weight="600" fill="#1a77c0">Tarvoon</text>
    </svg>
  </section>
</div>
</body>
</html>
```